Theatrical Producer/Consultant needs Artistic Brochure Shell and Inserts

Heron Stageworks (www.heronstageworks-example.com) is a small company that offers theatrical producing and consulting services. We would like to create a brochure that contains information about our various productions and services. Because our roster is fluid, we are proposing to create a brochure shell or folder with pockets, and then a template for individual tear sheets that would be inserted into the inside pockets of the brochure shell/folder. The shell is intended for reuse each season, and new tear sheets will be developed separately on a project by project basis.
This task is to create the shell and a corresponding tear sheet template.
The brochure will be delivered by hand as well as by mail, so should fit into a standard size mailing envelope (i.e., within NPMS flat dimensions of 6 1/8" x 11 1/2")
The final design should reflect the high level of artistry of our theatrical projects. Attached are our logo as well as photos of current theatrical offerings which are available for use on the brochure shell but not required. There is also a file that describes our services in more detail, fyi. This will ultimately go onto one of the tear sheets in the brochure.
For the tear sheet template, we have also included a sample brochure from a peer colleague, just to give you an idea of the kind of information each sheet would contain. Each project page will contain title of the project, information about the artists involved, one or more photos, a project description, schedule, fee and other technical information.
The final files for both the shell and tear sheet templates should be printer-ready and also in a file format that we can edit ourselves in future.
Updates
Project Deadline Extended Reason: There was a discrepancy between posted project deadline (December 7) and when project was automatically closed (December 6). Since several designers who have not yet submitted indicated they were planning to submit designs, we wanted to make sure that they were able to do so. Added Monday, December 7, 2015
Industry/Entity Type
Performing Art
Font styles to use
Look and feel
Each slider illustrates characteristics of the customer's brand and the style your logo design should communicate.

```html
<!DOCTYPE html>
<html lang="en">
<head>
<meta charset="utf-8">
<title>Heron Stageworks – Trifold Brochure</title>
<link href="https://fonts.googleapis.com/css2?family=Questrial&family=Sulphur+Point:wght@300;400;700&display=swap" rel="stylesheet">
<style>
  :root {
    --teal: #1a9aa6;
    --teal-deep: #0e6f79;
    --ink: #3a3a3a;
    --paper: #f2f2f1;
    --paper-shade: #e6e6e4;
    --stage: #9a9a9a;
    --photo-dark: #1e2a30;
    --white: #ffffff;
  }
  * { box-sizing: border-box; margin: 0; padding: 0; }
  html, body { width: 1200px; height: 761px; overflow: hidden; }
  body {
    background: radial-gradient(ellipse at 50% 20%, #e4e4e4 0%, #a8a8a8 70%, var(--stage) 100%);
    font-family: "Questrial", sans-serif;
    color: var(--ink);
    position: relative;
  }
  .brochure {
    position: absolute;
    left: 105px; top: 40px;
    width: 990px; height: 680px;
    display: flex;
    box-shadow: 0 14px 30px rgba(0,0,0,.35);
  }
  .panel { position: relative; width: 330px; height: 680px; overflow: hidden; }
  .panel--service { background: linear-gradient(90deg, var(--paper) 0%, var(--paper-shade) 100%); }
  .panel--portfolio { background: linear-gradient(90deg, #f8f8f8 0%, var(--paper) 100%); }
  .panel--cover { background: var(--photo-dark); }

  .section-title {
    position: absolute;
    font-family: "Sulphur Point", sans-serif;
    font-weight: 300;
    font-size: 22px;
    letter-spacing: 1.5px;
    text-transform: uppercase;
    color: var(--ink);
  }
  .rule { position: absolute; height: 3px; background: var(--teal); }
  .rule--white { background: var(--white); }

  .photo { position: absolute; }
  .service-block { position: absolute; left: 122px; width: 198px; }
  .service-block h3 {
    font-family: "Sulphur Point", sans-serif;
    font-weight: 400;
    font-size: 15px;
    letter-spacing: 1px;
    text-transform: uppercase;
    color: var(--teal);
  }
  .service-block .rule { position: static; display: block; width: 30px; height: 2px; margin: 4px 0 8px; }
  .body-text { font-size: 9.5px; line-height: 1.45; }
  .body-text + .body-text { margin-top: 8px; }

  .teal-wedge { position: absolute; inset: 0; }
  .service-content { position: absolute; inset: 0; }

  .brand-mark {
    position: absolute;
    display: flex; align-items: center; gap: 8px;
    font-family: "Questrial", sans-serif;
    color: var(--ink);
  }
  .brand-mark .dot { border-radius: 50%; border: 3px solid var(--teal); flex: none; }
  .brand-mark--large {
    left: 10px; top: 478px; width: 100px;
    flex-direction: column; gap: 6px;
    font-size: 12px; line-height: 1.3; text-align: center;
  }
  .brand-mark--large .dot { width: 80px; height: 80px; border-width: 6px; }
  .brand-mark--small { right: 22px; bottom: 44px; font-size: 17px; }
  .brand-mark--small .dot { width: 22px; height: 22px; }

  .cover-photo { position: absolute; inset: 0; }
  .cover-headline {
    position: absolute; left: 38px; top: 420px;
    font-family: "Sulphur Point", sans-serif;
    font-weight: 300;
    font-size: 21px; line-height: 1.45;
    letter-spacing: 1.5px;
    text-transform: uppercase;
    color: var(--white);
  }

  .portfolio-grid {
    position: absolute; left: 28px; top: 92px;
    display: grid; grid-template-columns: 130px 130px; column-gap: 14px; row-gap: 14px;
  }
  .portfolio-item .thumb { width: 130px; height: 78px; }
  .portfolio-item p { font-size: 8.5px; line-height: 1.45; margin-top: 6px; text-align: center; }
  .client-intro { position: absolute; left: 28px; top: 400px; width: 280px; }
  .client-intro .section-title { position: static; font-size: 20px; }
  .client-intro .rule { position: static; display: block; width: 34px; margin: 5px 0 14px; }
  .client-intro .body-text { font-size: 9.5px; line-height: 1.55; }
  .client-intro strong { color: var(--teal); font-weight: 400; }
</style>
</head>
<body>
<main class="brochure">

  <section class="panel panel--service">
    <svg class="teal-wedge" width="330" height="680" viewBox="0 0 330 680" aria-hidden="true">
      <polygon points="330,618 330,680 296,680" fill="var(--teal)"/>
    </svg>
    <div class="service-content">
      <h2 class="section-title" style="left:40px;top:36px;">Our Service</h2>
      <span class="rule" style="left:40px;top:66px;width:32px;"></span>

      <div class="photo" role="img" aria-label="Stage production photo: ensemble of costumed actors dancing on a dark blue stage set" style="left:0;top:78px;width:110px;height:120px;background:linear-gradient(160deg,#2c2446 0%,#4a3f6a 45%,#7a5a48 80%,#3a2c2a 100%);"></div>
      <span class="rule" style="left:36px;top:214px;width:34px;"></span>

      <div class="service-block" style="top:80px;">
        <h3>Producers</h3><span class="rule"></span>
        <p class="body-text">As producers we generate and develop our own innovative theatrical projects, serve as a creative producer for hire (by producing companies, independent artists and others) and provide other creative project-based services, including program development and dramaturgy.</p>
      </div>

      <div class="photo" role="img" aria-label="Performance photo: actor with dark hair in a close, emotional stage moment" style="left:0;top:242px;width:110px;height:186px;background:linear-gradient(150deg,#1f2a33 0%,#3b4650 40%,#8a7a70 70%,#2a3038 100%);"></div>
      <span class="rule" style="left:36px;top:446px;width:34px;"></span>

      <div class="service-block" style="top:238px;">
        <h3>Consultants</h3><span class="rule"></span>
        <p class="body-text">As consultants we work with theater companies, presenters, performing arts centers, foundations and other non-profit or commercial entities to provide ongoing programming advice, research and development as well as broad policy, leadership and structural input and oversight.</p>
        <p class="body-text">Our model of producing and consulting varies project-by-project, organization-by-organization. Our projects reflect a broad spectrum of genre, scale and clients. We examine the individual elements and/or artists involved and shape producing strategy around their particular visions. By customizing an approach that capitalizes on the strengths of everyone involved and then identifying how to supplement those strengths we facilitate artistic excellence, while having a good time.</p>
      </div>

      <div class="brand-mark brand-mark--large">
        <span class="dot"></span>
        <span>Heron Stageworks</span>
      </div>
    </div>
  </section>

  <section class="panel panel--cover">
    <div class="cover-photo" role="img" aria-label="Dramatic stage photo: two actors in close embrace, lit in cool tones" style="background:linear-gradient(170deg,#3d4a52 0%,#5d666c 30%,#2a363d 60%,#141d22 100%);"></div>
    <svg class="teal-wedge" width="330" height="680" viewBox="0 0 330 680" aria-hidden="true">
      <polygon points="85,285 330,280 330,300 230,680 0,680 0,520" fill="var(--teal)" opacity="0.72"/>
    </svg>
    <h2 class="cover-headline">We are good<br>at what we do<br>because we<br>are passionate<br>about it</h2>
    <span class="rule rule--white" style="left:40px;top:620px;width:40px;"></span>
  </section>

  <section class="panel panel--portfolio">
    <svg class="teal-wedge" width="330" height="680" viewBox="0 0 330 680" aria-hidden="true">
      <polygon points="0,300 48,300 0,440" fill="var(--teal)"/>
    </svg>
    <h2 class="section-title" style="left:28px;top:40px;">Our Portfolio</h2>
    <span class="rule" style="left:28px;top:70px;width:32px;"></span>

    <div class="portfolio-grid">
      <figure class="portfolio-item">
        <div class="thumb" role="img" aria-label="Production photo: puppet animal characters in costume on stage" style="background:linear-gradient(135deg,#2a2020 0%,#8a6a50 50%,#d8d0c8 75%,#3a3030 100%);"></div>
        <p>Lorem Ipsum. Proin gravida nibh vel velit auctor aliquet. Aenean</p>
      </figure>
      <figure class="portfolio-item">
        <div class="thumb" role="img" aria-label="Production photo: night scene with moon over a dark forest stage" style="background:linear-gradient(135deg,#101512 0%,#3a4a3a 50%,#a0a8a0 65%,#151a18 100%);"></div>
        <p>Lorem Ipsum. Proin gravida nibh vel velit auctor aliquet. Aenean</p>
      </figure>
      <figure class="portfolio-item">
        <div class="thumb" role="img" aria-label="Production photo: ornate stage set with ladder and curtains" style="background:linear-gradient(135deg,#5a2a20 0%,#a0684a 45%,#d0a070 65%,#4a2820 100%);"></div>
        <p>Lorem Ipsum. Proin gravida nibh vel velit auctor aliquet. Aenean</p>
      </figure>
      <figure class="portfolio-item">
        <div class="thumb" role="img" aria-label="Production photo: masked performers in dark costumes" style="background:linear-gradient(135deg,#121418 0%,#2e3440 50%,#8a8070 70%,#1a1c20 100%);"></div>
        <p>Lorem Ipsum. Proin gravida nibh vel velit auctor aliquet. Aenean</p>
      </figure>
    </div>

    <div class="client-intro">
      <h2 class="section-title">Become Client</h2>
      <span class="rule"></span>
      <p class="body-text">At its core, Heron combines artistic values with an independent flexibility and financial structure that allow us to create a body of work that wouldn't exist under any other auspice.</p>
      <p class="body-text"><strong>Heron Stageworks LLC</strong> strives to be nimble, adaptive and clever, all qualities we share with the noble heron.</p>
    </div>

    <div class="brand-mark brand-mark--small">
      <span class="dot"></span>
      <span>Heron Stageworks</span>
    </div>
  </section>

</main>
</body>
</html>
```